Business Card and Letterhead for Juniper Anvil - (Have Logo)

Update 4: Removed company reg no from business card details as it looked a bit out of place. Updated services list.
UPDATE 3
Sorry, I got the address a little bit wrong, have updated it below. Sorry for any inconvenience caused.
UPDATE 2
Finally I have the details for the business cards and letterhead. Submissions already made do not have to be updated unless shortlisted, if all new submissions could include the details for me, Marcus, that would be very much appreciated and help with the final shortlist selection. I intend to share a shortlist of the three best entries with past and existing customers for their feedback and opinions. Thank you all again for your time.
Here are the details.
Marcus Telby
Web Developer
T: 01632 960 418
E: marcus@juniperanvil.example
www.juniperanvil.example
Professional Photography
Web Solutions & E-Commerce
Audio & HD Video Production
Marketing & Promotions
Identity and Branding
Juniper Anvil Ltd
Suite 20938, 3rd Floor
212-224 Orchard Lane
London, N7 9QX
Company Reg. No: 05829147
The order and the layout of the information are of course down to the design, but the company registration number should be smaller and less prominent. The formatting of the telephone and email address using a T: and an E: I am not sure about and again if it is Tel: or Email: or Icons is up to the design.
The Company No. on the letterhead should read (somewhere in small text along the bottom):
Juniper Anvil is a Ltd Company registered in England & Wales, Registration No. 05829147.
The second business card details are
Oliver Brackley
Photographer
T: 01632 960 418
E: oliver@juniperanvil.example
Everything else the same of course.
Thank you again for all the submissions so far.
END OF UPDATE 2
-
UPDATE 1: Please do not alter the logo nor the logo colours. (This was a previous pixel forum project and I am extremely happy with it. The icon can stand alone of course, but I have had to eliminate all entries that have made it black and white, or reversed the icon.) I would like to thank everyone that has participated so far and am very grateful for all your thought and time.
End of Update 1
-
Original Brief:
I have attached the logo vector file.
Following a superb logo from a previous Pixel Forum project I am now looking for a business card design and (although less important) a letterhead as well.
I must admit I tried to do it myself but could only come up with the usual amateur stuff that in comparison to the quality of the logo looked awful.
About Us
Juniper Anvil Ltd will be a new company due to start in January. It is really just me (a web developer) and my friend (a photographer). We will be aiming at the usual small to medium sized businesses in the local area, selling various digital services including photographic services to the public, web hosting and development, commercial photography, modelling services (not us!), full video and film production and possibly a bit of marketing as well. (Really it is anything we can do professionally all lumped together! We met running seperate businesses which have both since closed)
We will not be competing on price. We plan to be expensive but fair. Certainly not the cheapest.
What we are looking for
Business Card
I imagine a double sided business card, which will be used for more than one person. I imagine the front to be the same for everyone and the persons details to be on the back, although this is of course only my thoughts and I am of course completely open to any ideas.
The card could also have a services list or a bit about what we do on it. It might feature the website address, our business address (mail forwarding address) or our registered company number.
Or it might have none of that, we are completely open to any ideas and have no real fixed opinions. I just want it to be really nice :-)
Letterhead (secondary importance)
We will make our decision primarily on the business card, although a mathcing letterhead would be fantastic. Something standardish in format and simple, although again, all ideas are welcomed.
I hope that is enough information but if you have any questions I will answer them as fully and as quickly as possible.
Thank you once again and I really look forward to seeing your ideas and picking a winner.
Marcus T.
Small businesses AND the general public
Film Production

```html
<!DOCTYPE html>
<html lang="en">
<head>
<meta charset="utf-8">
<title>Juniper Anvil — Stationery</title>
<link rel="stylesheet" href="https://fonts.googleapis.com/css2?family=Arimo:ital,wght@0,400;0,700;1,400;1,700&family=Archivo+Narrow:wght@700&display=swap">
<style>
  :root {
    --paper: #ffffff;
    --card: #000000;
    --red: #c1121f;
    --red-soft: #e9a8a8;
    --red-dark: #7a0f14;
    --grey: #4a4a4c;
    --grey-text: #555555;
    --ink: #1a1a1a;
    --white: #ffffff;
  }
  * { box-sizing: border-box; margin: 0; padding: 0; }
  html, body { width: 1200px; height: 900px; overflow: hidden; background: var(--paper); }
  body { position: relative; font-family: "Arimo", Arial, sans-serif; }

  .presentation {
    position: absolute; left: 18px; top: 18px; width: 1162px; height: 866px;
    border-radius: 90px; background: var(--paper);
    box-shadow: 0 0 14px rgba(0,0,0,.28);
  }

  /* Letterhead */
  .letterhead {
    position: absolute; left: 97px; top: 30px; width: 569px; height: 806px;
    background: var(--paper); border: 1px solid #dcdcdc;
  }
  .abs { position: absolute; white-space: nowrap; }
  .lh-mark { left: 173px; top: 98px; display: flex; align-items: center; gap: 7px; }
  .lh-mark .square { width: 20px; height: 20px; background: var(--red); }
  .lh-mark .name { font-weight: 700; font-size: 19px; color: var(--grey); letter-spacing: .5px; }
  .lh-bracket { position: absolute; background: var(--red-soft); }
  .lh-contact { font-size: 8px; letter-spacing: 1.1px; color: var(--grey-text); text-transform: uppercase; line-height: 10px; }
  .lh-contact.email { font-size: 7.5px; letter-spacing: .4px; }
  .lh-contact.person { color: var(--red); font-weight: 700; }
  .salutation { left: 49px; top: 248px; font-size: 10px; font-weight: 700; letter-spacing: 1.2px; color: var(--ink); }
  .body-copy {
    position: absolute; left: 75px; top: 297px; width: 440px; height: 120px; overflow: hidden;
    font-size: 11px; line-height: 12.8px; letter-spacing: .5px; color: #222;
  }
  .closing { left: 437px; top: 664px; font-size: 10px; font-weight: 700; letter-spacing: 1.2px; color: var(--ink); }
  .signature { position: absolute; left: 418px; top: 674px; width: 72px; height: 66px; background: linear-gradient(135deg, #f4f4f4, #e6e6e6); }
  .legal { left: 49px; top: 778px; font-size: 7.6px; letter-spacing: 1.1px; color: var(--grey-text); }

  /* Cards */
  .card {
    position: absolute; background: var(--card); overflow: hidden;
    box-shadow: 2px 3px 6px rgba(0,0,0,.45);
  }
  .card-back { width: 255px; height: 364px; color: var(--white); }
  .services { position: absolute; list-style: none; font-family: "Archivo Narrow", "Arial Narrow", sans-serif; font-weight: 700; font-size: 7px; letter-spacing: .5px; line-height: 14px; text-transform: uppercase; }
  .cb-line { position: absolute; background: var(--red-dark); }
  .cb-text { position: absolute; white-space: nowrap; font-size: 9px; line-height: 11px; letter-spacing: .3px; text-transform: uppercase; }
  .cb-small { font-family: "Archivo Narrow", "Arial Narrow", sans-serif; font-weight: 700; font-size: 7px; letter-spacing: .4px; }
  .cb-name { color: var(--red); font-weight: 700; font-size: 9px; letter-spacing: .6px; }
  .cb-name em { font-style: italic; }
  .cb-role { color: var(--grey); font-weight: 700; font-size: 8.5px; letter-spacing: .6px; }
  .cb-mark { position: absolute; display: flex; flex-direction: column; align-items: flex-start; gap: 3px; }
  .cb-mark .square { width: 14px; height: 14px; background: var(--red); }
  .cb-mark .name { font-weight: 700; font-size: 7px; line-height: 8px; color: var(--grey); text-transform: uppercase; letter-spacing: .3px; }

  .card-front { color: var(--white); }
  .hero-name { position: absolute; left: 0; right: 0; text-align: center; font-weight: 700; color: var(--red); text-transform: uppercase; letter-spacing: 1px; }
  .tagline { position: absolute; left: 0; right: 0; text-align: center; color: var(--red); font-weight: 700; text-transform: uppercase; letter-spacing: 1px; }
  .foot-mark { position: absolute; display: flex; align-items: center; gap: 5px; }
  .foot-mark .square { background: var(--red); }
  .foot-mark .name { font-weight: 700; color: var(--grey); text-transform: uppercase; letter-spacing: .4px; }
</style>
</head>
<body>
<div class="presentation"></div>

<section class="letterhead" aria-label="Letterhead">
  <div class="abs lh-mark"><span class="square"></span><span class="name">JUNIPER ANVIL</span></div>
  <div class="lh-bracket" style="left:335px;top:16px;width:33px;height:1px"></div>
  <div class="lh-bracket" style="left:368px;top:16px;width:1px;height:199px"></div>
  <div class="lh-bracket" style="left:335px;top:215px;width:33px;height:1px"></div>
  <div class="lh-bracket" style="left:368px;top:116px;width:32px;height:1px"></div>
  <div class="abs lh-contact" style="left:410px;top:56px">T. 01632 960 418</div>
  <div class="abs lh-contact email" style="left:410px;top:73px">marcus@juniperanvil.example</div>
  <div class="abs lh-contact person" style="left:410px;top:111px">Marcus Telby</div>
  <div class="abs lh-contact" style="left:410px;top:138px">Co #. 05829147</div>
  <div class="abs lh-contact" style="left:410px;top:156px">Suite 20938, 3rd Floor<br>212-224 Orchard Lane</div>
  <div class="abs lh-contact" style="left:410px;top:184px">London,<br>N7 9QX</div>
  <div class="abs salutation">VALUED CLIENT,</div>
  <p class="body-copy">Lorem ipsum dolor sit amet, consectetur adipiscing elit. Nullam lorem ultrices interdum. Curabitur nulla sapien, eleifend vel malesuada at nibh. Nullam volutpat pulvinar nibh. Lorem ipsum dolor sit amet, consectetur adipiscing elit. Donec molestie. Nullam erat leo, elementum sit amet tincidunt nec, et velit. Mauris ante dolor, tristique pretium lacinia et, urna. In erat est, dignissim nec placerat vitae, semper at. Morbi euismod porttitor luctus. Duis accumsan.</p>
  <div class="abs closing">SINCERELY,</div>
  <div class="signature" role="img" aria-label="Handwritten signature"></div>
  <div class="abs legal">JUNIPER ANVIL IS A LTD COMPANY REGISTERED IN ENGLAND &amp; WALES, REGISTRATION NO. 05829147.</div>
</section>

<section class="card card-front" style="left:397px;top:295px;width:255px;height:360px;transform:rotate(4deg)" aria-label="Business card front">
  <div class="hero-name" style="top:60px;font-size:22px;line-height:24px">Juniper<br>Anvil</div>
  <p class="tagline" style="top:178px;font-size:10px;line-height:13px">Your ideas, our craft -<br>made sharper &amp; more memorable.</p>
  <div class="foot-mark" style="left:50px;top:318px"><span class="square" style="width:12px;height:12px"></span><span class="name" style="font-size:12px">Juniper Anvil</span></div>
</section>

<section class="card card-back" style="left:158px;top:424px" aria-label="Business card back, Oliver Brackley">
  <div class="cb-line" style="left:7px;top:69px;width:50px;height:1px"></div>
  <div class="cb-line" style="left:57px;top:69px;width:1px;height:289px"></div>
  <div class="cb-line" style="left:7px;top:358px;width:50px;height:1px"></div>
  <div class="cb-line" style="left:45px;top:214px;width:65px;height:1px"></div>
  <ul class="services" style="left:114px;top:67px">
    <li>Professional Photography</li><li>Web Solutions &amp; E-Commerce</li><li>Audio &amp; HD Video Production</li><li>Marketing &amp; Promotions</li><li>Design, Creation and Inspiration</li>
  </ul>
  <div class="cb-text" style="left:114px;top:151px">T. 01632 960 418</div>
  <div class="cb-text cb-small" style="left:114px;top:171px">oliver@juniperanvil.example</div>
  <div class="cb-mark" style="left:7px;top:186px"><span class="square"></span><span class="name">Juniper<br>Anvil</span></div>
  <div class="cb-text cb-name" style="left:114px;top:209px"><em>Oliver Brackley</em></div>
  <div class="cb-text cb-small" style="left:114px;top:238px">Co #. 05829147</div>
  <div class="cb-text" style="left:114px;top:259px">Suite 20938, 3rd Floor<br>212-224 Orchard Lane</div>
  <div class="cb-text" style="left:114px;top:290px">London,<br>N7 9QX</div>
  <div class="cb-text cb-small" style="left:114px;top:320px">www.juniperanvil.example</div>
</section>

<section class="card card-back" style="left:754px;top:50px" aria-label="Business card back, Marcus Telby">
  <div class="cb-line" style="left:196px;top:70px;width:50px;height:1px"></div>
  <div class="cb-line" style="left:196px;top:70px;width:1px;height:289px"></div>
  <div class="cb-line" style="left:196px;top:359px;width:50px;height:1px"></div>
  <div class="cb-line" style="left:150px;top:214px;width:60px;height:1px"></div>
  <ul class="services" style="left:58px;top:67px">
    <li>Professional Photography</li><li>Web Solutions &amp; E-Commerce</li><li>Audio &amp; HD Video Production</li><li>Marketing &amp; Promotions</li><li>Design, Creation and Inspiration</li>
  </ul>
  <div class="cb-text" style="left:58px;top:151px">T. 01632 960 418</div>
  <div class="cb-text cb-small" style="left:58px;top:171px">marcus@juniperanvil.example</div>
  <div class="cb-mark" style="left:211px;top:186px"><span class="square"></span><span class="name">Juniper<br>Anvil</span></div>
  <div class="cb-text cb-name" style="left:58px;top:209px">Marcus <em>Telby</em></div>
  <div class="cb-text cb-role" style="left:58px;top:220px">Web Developer</div>
  <div class="cb-text cb-small" style="left:58px;top:249px">Co #. 05829147</div>
  <div class="cb-text" style="left:58px;top:269px">Suite 20938, 3rd Floor<br>212-224 Orchard Lane</div>
  <div class="cb-text" style="left:58px;top:300px">London,<br>N7 9QX</div>
  <div class="cb-text cb-small" style="left:58px;top:330px">www.juniperanvil.example</div>
</section>

<section class="card card-front" style="left:802px;top:438px;width:245px;height:358px;transform:rotate(-19deg)" aria-label="Business card front">
  <div class="hero-name" style="top:62px;font-size:22px;line-height:24px">Juniper<br>Anvil</div>
  <p class="tagline" style="top:186px;font-size:10px;line-height:13px">Your ideas, our craft -<br>made sharper &amp; more memorable.</p>
  <div class="foot-mark" style="left:60px;top:318px"><span class="square" style="width:12px;height:12px"></span><span class="name" style="font-size:12px">Juniper Anvil</span></div>
</section>
</body>
</html>
```